D*mn Those Cozy Walls - Dare Boldly, Claim Center Stage Within Every Day: UPCOMING BOOK

We want a Book Cover for a book that will be published shortly. Some options we originally created are attached but they are not really working but give an idea of the text that needs to be on there. We want it to look like a quality book. Tessa is a well known acting coach, and we have some amazing celebrity quotes for the front cover - but it doesn't HAVE to reflect the acting world, the book is for everyone. We want something that represents freedom a sense of release, INSPIRATIONAL - but not cheesy. No flowers or images like that. Simple and authentic is best... Happy to try some with text only and just block colors - the title needs to POP. It's long but we want the Dare Boldly part to pop as well.

```html
<!DOCTYPE html>
<html lang="en">
<head>
<meta charset="UTF-8">
<title>D*mn Those Cozy Walls – Book Cover</title>
<link href="https://fonts.googleapis.com/css2?family=Montserrat:ital,wght@0,300;0,600;0,700;0,800;1,300&display=swap" rel="stylesheet">
<style>
  :root {
    --backdrop: #ebe9e5;
    --coral: #f37a5c;
    --coral-light: #f6a084;
    --teal: #03464f;
    --teal-deep: #023a42;
    --yellow: #fdf07c;
    --white: #ffffff;
  }
  * { margin: 0; padding: 0; box-sizing: border-box; }
  html, body {
    width: 1200px;
    height: 922px;
    overflow: hidden;
    background: var(--backdrop);
    font-family: "Montserrat", Arial, sans-serif;
  }
  .cover {
    position: absolute;
    left: 313px;
    top: 31px;
    width: 573px;
    height: 860px;
    background: linear-gradient(135deg, var(--coral-light) 0%, var(--coral) 45%, var(--coral) 100%);
    overflow: hidden;
    box-shadow: 0 4px 18px rgba(0,0,0,0.12);
  }
  .author {
    position: absolute;
    top: 38px;
    width: 100%;
    text-align: center;
    color: var(--yellow);
    font-weight: 800;
    font-size: 41px;
    letter-spacing: 0.5px;
    line-height: 1;
  }
  .author-role {
    position: absolute;
    top: 86px;
    width: 100%;
    text-align: center;
    color: var(--white);
    font-weight: 300;
    font-style: italic;
    font-size: 24px;
    letter-spacing: 0.5px;
  }
  .title-disc {
    position: absolute;
    left: 25px;
    top: 139px;
    width: 522px;
    height: 522px;
    border-radius: 50%;
    background: radial-gradient(circle at 50% 40%, var(--teal) 0%, var(--teal-deep) 100%);
  }
  .title {
    position: absolute;
    top: 172px;
    width: 100%;
    text-align: center;
    font-weight: 800;
    font-size: 66px;
    line-height: 56px;
    letter-spacing: -0.5px;
  }
  .title span { display: block; }
  .title .light { color: var(--white); }
  .title .accent { color: var(--yellow); }
  .rule {
    position: absolute;
    left: 258px;
    top: 424px;
    width: 58px;
    height: 2px;
    background: var(--yellow);
  }
  .subtitle {
    position: absolute;
    top: 442px;
    width: 100%;
    text-align: center;
    color: var(--yellow);
    font-weight: 700;
    font-size: 17px;
    line-height: 23px;
    letter-spacing: 0.2px;
  }
  .chair-art {
    position: absolute;
    left: 213px;
    top: 497px;
    width: 150px;
    height: 258px;
  }
  .endorsement {
    position: absolute;
    top: 782px;
    width: 100%;
    text-align: center;
    color: var(--white);
  }
  .endorsement .quote {
    font-weight: 300;
    font-style: italic;
    font-size: 21px;
    letter-spacing: 0.3px;
  }
  .endorsement .source {
    margin-top: 2px;
    font-weight: 600;
    font-size: 19px;
  }
</style>
</head>
<body>
  <main class="cover">
    <h2 class="author">TESSA CALLOWAY</h2>
    <p class="author-role">Hollywood's #1 Acting Coach</p>

    <div class="title-disc"></div>
    <h1 class="title">
      <span class="light">D*MN</span>
      <span class="accent">THOSE</span>
      <span class="light">COZY</span>
      <span class="accent">WALLS</span>
    </h1>
    <div class="rule"></div>
    <p class="subtitle">DARE BOLDLY, CLAIM CENTER STAGE<br>WITHIN EVERY DAY</p>

    <svg class="chair-art" role="img" aria-label="Line illustration of a folding director's chair" viewBox="0 0 150 258">
      <rect x="0" y="0" width="150" height="258" rx="6" fill="#fdf07c" opacity="0.35"/>
    </svg>

    <div class="endorsement">
      <p class="quote">"I f*ucking love this book ...."</p>
      <p class="source">Renata Vale</p>
    </div>
  </main>
</body>
</html>
```